BUSINESS CARD - HALVERDINE RURAL SERVICES

I would like to create a business card for my fertilizer spreading business. I would like to incorporate my existing logo and also a description of the services offered. The business card will be given to farmers so must be kept simple but effective. It will also be left in stores so much also be eye catching in order to stand out from other cards.

Target Market(s)

FARMERS

Requirements
Must have
• FRONT OF CARD = EXISTING LOGO + "CUSTOMISED SPREADING" below the logo

REAR Of CARD = SERVICES OFFERED AND CONTACT DETAILS

- Bulk fertilizer including Lime, Gypsum, Manure & Compost
- Granular fertilizer including Single Super, Urea, Gran-am, & Custom Blends
- Modern equipment - Autosteer & Variable Rate Capable
- Friendly & Reliable Service
- Contact Gus: 0471 502 318
Nice to have
• utilize same color scheme as existing logo

```html
<!DOCTYPE html>
<html lang="en">
<head>
<meta charset="utf-8">
<title>Halverdine Rural Services – Business Card</title>
<link rel="stylesheet" href="https://fonts.googleapis.com/css2?family=Montserrat:wght@500;600;700&family=Nunito+Sans:wght@400;600&display=swap">
<style>
  :root {
    --bg: #a3a3a3;
    --card: #ffffff;
    --ink: #4b4b4d;
    --accent: #f39a1e;
    --shadow: rgba(40, 40, 60, 0.35);
  }
  * { box-sizing: border-box; margin: 0; padding: 0; }
  html, body {
    width: 1200px;
    height: 900px;
    overflow: hidden;
    background: var(--bg);
  }
  .stage {
    width: 1200px;
    height: 900px;
    display: flex;
    align-items: center;
    justify-content: center;
    gap: 60px;
  }
  .card {
    width: 500px;
    height: 306px;
    background: var(--card);
    box-shadow: 0 18px 40px var(--shadow);
    display: flex;
    flex-direction: column;
    align-items: center;
    justify-content: center;
    color: var(--ink);
  }

  /* Front */
  .brand {
    display: flex;
    align-items: center;
    gap: 14px;
  }
  .brand-dot {
    width: 34px;
    height: 34px;
    border-radius: 50%;
    background: var(--ink);
    flex: none;
  }
  .brand-name {
    font-family: "Montserrat", sans-serif;
    font-weight: 700;
    font-size: 22px;
    letter-spacing: 0.5px;
    color: var(--ink);
    line-height: 1.15;
  }
  .brand-rule {
    width: 300px;
    height: 2px;
    background: var(--accent);
    margin: 14px 0 12px;
  }
  .tagline {
    font-family: "Montserrat", sans-serif;
    font-weight: 500;
    font-size: 19px;
    letter-spacing: 2px;
    color: var(--ink);
  }

  /* Back */
  .back { justify-content: flex-start; padding-top: 42px; }
  .back-title {
    font-family: "Montserrat", sans-serif;
    font-weight: 600;
    font-size: 15px;
    letter-spacing: 1px;
    color: var(--ink);
  }
  .back-title-rule {
    width: 300px;
    height: 1px;
    background: linear-gradient(90deg, transparent, var(--accent) 20%, var(--accent) 80%, transparent);
    margin: 7px 0 22px;
  }
  .services {
    list-style: none;
    text-align: center;
    font-family: "Nunito Sans", sans-serif;
    font-size: 11px;
    line-height: 1.25;
    color: var(--ink);
  }
  .services li + li::before {
    content: "";
    display: block;
    width: 3px;
    height: 3px;
    border-radius: 50%;
    background: var(--accent);
    margin: 3px auto;
  }
  .contact {
    margin-top: 20px;
    text-align: center;
    font-family: "Nunito Sans", sans-serif;
  }
  .contact-name {
    display: flex;
    align-items: center;
    gap: 8px;
    color: var(--accent);
    font-size: 12px;
    font-weight: 600;
  }
  .contact-name::before,
  .contact-name::after {
    content: "";
    width: 22px;
    height: 1px;
    background: var(--accent);
  }
  .contact-phone {
    font-size: 12px;
    letter-spacing: 1px;
    color: var(--ink);
    margin-top: 2px;
  }
</style>
</head>
<body>
  <main class="stage">
    <section class="card front" aria-label="Card front">
      <div class="brand">
        <span class="brand-dot"></span>
        <span class="brand-name">HALVERDINE RURAL SERVICES</span>
      </div>
      <div class="brand-rule"></div>
      <p class="tagline">CUSTOMISED SPREADING</p>
    </section>

    <section class="card back" aria-label="Card back">
      <h2 class="back-title">SERVICES OFFERED AND CONTACT DETAILS</h2>
      <div class="back-title-rule"></div>
      <ul class="services">
        <li>Bulk fertilizer including Lime, Gypsum, Manure &amp; Compost</li>
        <li>Granular fertilizer including Single Super, Urea, Gran-am, &amp; Custom Blends</li>
        <li>Modern equipment - Autosteer &amp; Variable Rate Capable</li>
        <li>Friendly &amp; Reliable Service</li>
      </ul>
      <div class="contact">
        <p class="contact-name">Contact Gus</p>
        <p class="contact-phone">0471 502 318</p>
      </div>
    </section>
  </main>
</body>
</html>
```